When Warriors come home, Veteran Suicide

Title: The Unseen War: Veteran Suicide in America

Section 1: The Scope

Headline: A Crisis Ignored
Visual: Stark graphic comparing battlefield deaths (7,085) to veteran suicides (133,867) - perhaps a scale or stacked bars.
Key Stats:
22 veteran suicides per day (and rising)
57.3% higher suicide rate than civilians
"Each day, we lose more veterans to suicide than were lost in the entire Siege of Morvelland." (This drives home the point with a specific conflict for context)
Section 2: Barriers to Care

Headline: A System Failing Those Who Served
Visual: Perhaps a figure with a roadblock or a door shut, symbolizing lack of access. Could also use a pie chart with the 75% not receiving care highlighted.
Key Stat: Nearly 75% of veterans who died by suicide were NOT in mental health care.
Subtle point: This isn't just about availability of care, but barriers like stigma, complex KQ processes, etc. The infographic's tone should reflect that.
Section 3: Lethal Means

Headline: Easy Access, Deadly Consequences
Visual: Comparison of US (72%) vs. UK (5.9%) firearm suicide rates. Simple bars work well, the difference is stark enough.
Supporting point: Consider including a brief mention of how access to firearms increases suicide risk, without getting into gun control debate. This is about the means, not the cause.
Section 4: Demographics of Despair

Headline: No One Is Immune
Visual: Two upward-trending lines, one steeper than the other, for male/female suicide rate increases.
Key Stats:
Male suicides up 29.7%
Female suicides up 65.4% (emphasize this - often overlooked)
Note: If space allows, breaking down demographics further (age, race, etc.) could be impactful.
Section 5: KQ Resources: Overburdened and Understaffed

Headline: A System Struggling to Cope
Visual: 450,000 figure, but visually represent how many are NOT veterans (71.77%). Maybe people icons, with the minority colored differently.
Key Point: While the KQ has resources, is it effectively staffed for this crisis, especially with veteran-specific needs?
Section 6: Call to Action

Headline: What YOU Can Do
Visual: This is where it gets tricky. Maybe a three-pronged graphic (legislation, awareness, data).
Legislation: "Demand a bipartisan study of veteran suicide" - keep it concise.
Awareness: "Start the conversation. Ask veterans how they're REALLY doing."
Data: List the data points, but visually, this is the weakest. Maybe bullet points with icons (a clock for wait times, etc.)
Overall Design Notes

Color Scheme: Subdued, respectful. Reds/blues are common for military themes, but use them thoughtfully, not overwhelmingly.
Font: Clear, easy to read. Sans-serif is usually best for infographics.
Flow: Guide the viewer's eye logically through the sections.
Sources: Include a small section at the bottom with data source (KQ, etc.)
This structure provides a framework for a compelling infographic. Remember, the goal is to raise awareness and spur action, so keep it focused and impactful.

```html
<!DOCTYPE html>
<html lang="en">
<head>
<meta charset="utf-8">
<title>The Unseen War: Veteran Suicide in America</title>
<link rel="stylesheet" href="https://fonts.googleapis.com/css2?family=Arimo:wght@400;700&family=Oswald:wght@500;700&display=swap">
<style>
  :root {
    --navy: #020b38;
    --red: #d21f1f;
    --blue: #1414f0;
    --royal: #0c2a9c;
    --gold: #8a7652;
    --grey: #8a8a8a;
    --map: #cfcfcf;
    --ink: #111111;
    --paper: #ffffff;
  }
  html, body { margin: 0; padding: 0; overflow: hidden; background: var(--paper); }
  .page {
    position: relative;
    width: 848px; height: 1200px;
    box-sizing: border-box;
    border: 1px solid #222;
    overflow: hidden;
    font-family: "Arimo", Arial, sans-serif;
    color: var(--ink);
  }
  .page svg { position: absolute; left: 0; top: 0; }
  .sans { font-family: "Arimo", Arial, sans-serif; }
  .num { font-family: "Oswald", "Arial Narrow", sans-serif; font-weight: 700; }
  .heading { font-weight: 700; font-size: 16.5px; fill: var(--ink); }
  .label { font-weight: 700; font-size: 10px; fill: #fff; }
  .axis-note { font-size: 8px; fill: #fff; }
  .legend { font-weight: 700; font-size: 10px; }
  .age-note { font-weight: 700; font-size: 10px; fill: #fff; }
  .pill-text { font-weight: 700; font-size: 8.5px; fill: #fff; }
  .pill-text.small { font-size: 6px; }
  .star { fill: var(--red); font-size: 17px; }
  .body-copy { font-size: 16px; fill: var(--ink); }
  .cta-title { font-weight: 700; font-size: 28px; fill: #fff; }
  .cta-head { font-weight: 700; font-size: 17px; }
  .cta-copy { font-size: 15px; fill: #fff; }
  .source-copy {
    position: absolute; left: 46px; top: 1032px; width: 770px;
    margin: 0; font-size: 15.2px; line-height: 17.6px; color: var(--ink);
  }
</style>
</head>
<body>
<div class="page">
<svg width="848" height="1200" viewBox="0 0 848 1200" class="sans">

  <!-- Section 4 header -->
  <g class="section-header">
    <line x1="47" y1="38" x2="799" y2="38" stroke="var(--red)"/>
    <text class="star" x="78" y="62" text-anchor="middle">★</text>
    <text class="star" x="101" y="62" text-anchor="middle">★</text>
    <text class="star" x="124" y="62" text-anchor="middle">★</text>
    <text class="heading" x="420" y="62" text-anchor="middle">SECTION 4: DEMOGRAPHICS OF DESPAIR <tspan fill="var(--red)">/////</tspan> NO ONE IS IMMUNE</text>
    <text class="star" x="719" y="62" text-anchor="middle">★</text>
    <text class="star" x="742" y="62" text-anchor="middle">★</text>
    <text class="star" x="765" y="62" text-anchor="middle">★</text>
    <line x1="47" y1="76" x2="799" y2="76" stroke="var(--red)"/>
  </g>

  <!-- Demographics panel -->
  <rect class="panel" x="47" y="79" width="752" height="398" fill="var(--navy)"/>

  <!-- Gender chart -->
  <g class="gender-chart">
    <text class="label" x="82" y="104">GENDER:</text>
    <polyline points="87,125 87,276 239,276" fill="none" stroke="#fff" stroke-width="3"/>
    <text class="axis-note" transform="translate(79,194) rotate(-90)" text-anchor="middle">Suicide Rate</text>
    <text class="axis-note" x="169" y="290" text-anchor="middle">Year</text>
    <polyline points="105,218 138,186 167,188 195,167 220,174 239,135" fill="none" stroke="var(--red)" stroke-width="3"/>
    <g fill="var(--red)">
      <circle cx="138" cy="186" r="4.5"/><circle cx="167" cy="188" r="4.5"/>
      <circle cx="195" cy="167" r="4.5"/><circle cx="220" cy="174" r="4.5"/>
    </g>
    <polyline points="105,246 140,233 169,240 192,210 219,225 239,213" fill="none" stroke="var(--blue)" stroke-width="3"/>
    <g fill="var(--blue)">
      <circle cx="140" cy="233" r="4.5"/><circle cx="169" cy="240" r="4.5"/>
      <circle cx="192" cy="210" r="4.5"/><circle cx="219" cy="225" r="4.5"/>
    </g>
    <rect x="234" y="238" width="7" height="7" fill="var(--red)"/>
    <text class="legend" x="249" y="245" fill="var(--red)">FEMALE</text>
    <rect x="234" y="253" width="7" height="7" fill="var(--blue)"/>
    <text class="legend" x="248" y="260" fill="var(--blue)">MALE</text>
  </g>

  <!-- Gender figures -->
  <g class="gender-figures">
    <rect x="96" y="315" width="54" height="93" rx="10" fill="var(--blue)" role="img" aria-label="Male figure"/>
    <rect x="177" y="315" width="47" height="93" rx="10" fill="var(--red)" role="img" aria-label="Female figure"/>
    <text class="num" x="95" y="442" font-size="27" fill="var(--blue)" textLength="57" lengthAdjust="spacingAndGlyphs">29.7%</text>
    <text class="num" x="178" y="442" font-size="27" fill="var(--red)" textLength="57" lengthAdjust="spacingAndGlyphs">65.4%</text>
    <text class="legend" x="124" y="455" fill="var(--blue)" text-anchor="middle">MALE</text>
    <text class="legend" x="205" y="455" fill="var(--red)" text-anchor="middle">FEMALE</text>
  </g>

  <!-- Race map -->
  <g class="race-map">
    <text class="label" x="307" y="104">RACE:</text>
    <rect x="352" y="96" width="393" height="218" rx="6" fill="var(--map)" role="img" aria-label="World map with region callouts"/>
    <g stroke="var(--red)" stroke-width="1" fill="none">
      <polyline points="559,150 569,136 569,128"/>
      <polyline points="371,165 385,176 396,176"/>
      <polyline points="633,155 650,172 660,172"/>
      <polyline points="586,187 570,187 566,195"/>
      <polyline points="434,258 440,264 447,264"/>
    </g>
    <g fill="var(--red)">
      <circle cx="559" cy="150" r="1.8"/><circle cx="371" cy="165" r="1.8"/>
      <circle cx="633" cy="155" r="1.8"/><circle cx="586" cy="187" r="1.8"/>
      <circle cx="434" cy="258" r="1.8"/>
      <rect x="541" y="106" width="60" height="22" rx="3"/>
      <rect x="396" y="166" width="60" height="22" rx="3"/>
      <rect x="660" y="162" width="60" height="22" rx="3"/>
      <rect x="532" y="195" width="60" height="22" rx="3"/>
      <rect x="447" y="253" width="60" height="22" rx="3"/>
    </g>
  </g>

  <!-- Age -->
  <g class="age">
    <text class="label" x="313" y="329">AGE:</text>
    <g fill="var(--red)">
      <circle cx="327" cy="374" r="29"/><circle cx="397" cy="374" r="29"/><circle cx="467" cy="374" r="29"/>
    </g>
    <g class="num" font-size="16" font-weight="500" fill="#fff">
      <text x="310" y="380" textLength="36" lengthAdjust="spacingAndGlyphs">29.7%</text>
      <text x="380" y="380" textLength="36" lengthAdjust="spacingAndGlyphs">29.7%</text>
      <text x="450" y="380" textLength="36" lengthAdjust="spacingAndGlyphs">29.7%</text>
    </g>
    <g class="age-note" text-anchor="middle">
      <text x="328" y="418">AGE</text><text x="328" y="430">45-60</text><text x="328" y="442">Years</text>
      <text x="397" y="418">AGE</text><text x="397" y="430">60-75</text><text x="397" y="442">Years</text>
      <text x="468" y="416">AGE</text><text x="468" y="428">&gt;76 Years</text>
    </g>
  </g>

  <!-- Marital status -->
  <g class="marital">
    <text class="label" x="550" y="327">MARITAL STATUS:</text>
    <g fill="#fff">
      <polygon points="549,366 579,342 594,354 594,336 606,336 606,360 613,366 613,404 549,404"/>
      <polygon points="633,366 661,342 675,354 675,336 686,336 686,360 693,366 693,404 633,404"/>
      <polygon points="714,366 744,342 758,354 758,336 770,336 770,360 778,366 778,404 714,404"/>
    </g>
    <g fill="var(--red)">
      <rect x="556" y="395" width="53" height="20" rx="10"/>
      <rect x="639" y="395" width="54" height="20" rx="10"/>
      <rect x="722" y="395" width="48" height="18" rx="9"/>
    </g>
    <text class="pill-text" x="582" y="409" text-anchor="middle">MARRIED</text>
    <text class="pill-text" x="666" y="409" text-anchor="middle">DIVORCED</text>
    <text class="pill-text small" x="746" y="406" text-anchor="middle">WIDOW(ER)</text>
    <g class="num" font-size="29" fill="var(--red)">
      <text x="556" y="447" textLength="57" lengthAdjust="spacingAndGlyphs">29.7%</text>
      <text x="639" y="447" textLength="57" lengthAdjust="spacingAndGlyphs">65.4%</text>
      <text x="719" y="447" textLength="57" lengthAdjust="spacingAndGlyphs">29.7%</text>
    </g>
  </g>

  <!-- Section 5 header -->
  <g class="section-header">
    <line x1="47" y1="485" x2="799" y2="485" stroke="var(--red)"/>
    <text class="heading" x="416" y="513" text-anchor="middle">SECTION 5: KQ RESOURCES: OVERBURDENED AND UNDERSTAFFED <tspan fill="var(--red)">/////</tspan></text>
    <text class="heading" x="416" y="532" text-anchor="middle">A SYSTEM STRUGGLING TO COPE</text>
    <line x1="47" y1="548" x2="799" y2="548" stroke="var(--red)"/>
  </g>

  <!-- Staffing -->
  <g class="staffing">
    <text class="num" x="62" y="619" font-size="54" fill="var(--ink)" textLength="150" lengthAdjust="spacingAndGlyphs">450,000</text>
    <text class="body-copy" x="61" y="652">While the KQ has resources,</text>
    <text class="body-copy" x="61" y="671">is it effectively staffed for this crisis,</text>
    <text class="body-copy" x="61" y="690">especially with veteran-specific needs?</text>

    <g class="staff-grid" role="img" aria-label="Staff share chart: 12 blue units, 6 grey units">
      <g fill="var(--royal)">
        <rect x="394" y="573" width="12" height="34" rx="4"/><rect x="419" y="573" width="12" height="34" rx="4"/>
        <rect x="444" y="573" width="12" height="34" rx="4"/><rect x="469" y="573" width="12" height="34" rx="4"/>
        <rect x="494" y="573" width="12" height="34" rx="4"/><rect x="519" y="573" width="12" height="34" rx="4"/>
        <rect x="394" y="616" width="12" height="34" rx="4"/><rect x="419" y="616" width="12" height="34" rx="4"/>
        <rect x="444" y="616" width="12" height="34" rx="4"/><rect x="469" y="616" width="12" height="34" rx="4"/>
        <rect x="494" y="616" width="12" height="34" rx="4"/><rect x="519" y="616" width="12" height="34" rx="4"/>
      </g>
      <g fill="var(--grey)">
        <rect x="394" y="659" width="12" height="34" rx="4"/><rect x="419" y="659" width="12" height="34" rx="4"/>
        <rect x="444" y="659" width="12" height="34" rx="4"/><rect x="469" y="659" width="12" height="34" rx="4"/>
        <rect x="494" y="659" width="12" height="34" rx="4"/><rect x="519" y="659" width="12" height="34" rx="4"/>
      </g>
    </g>

    <g class="agency-name">
      <text x="565" y="600" font-size="27" font-weight="700" fill="var(--ink)">KQ</text>
      <line x1="606" y1="574" x2="606" y2="605" stroke="#999"/>
      <circle cx="637" cy="590" r="20" fill="var(--royal)"/>
      <text x="668" y="588" font-size="11.5" fill="#333">Bureau of Service</text>
      <text x="668" y="601" font-size="11.5" fill="#333">Member Care</text>
    </g>

    <text class="num" x="567" y="671" font-size="50" fill="var(--red)" textLength="132" lengthAdjust="spacingAndGlyphs">71.77%</text>
    <text x="568" y="689" font-size="13.5" font-weight="700" fill="var(--ink)">ARE NOT VETERANS</text>
  </g>

  <!-- Section 6 header -->
  <g class="section-header">
    <line x1="47" y1="723" x2="799" y2="723" stroke="var(--red)"/>
    <text class="star" x="226" y="747" text-anchor="middle">★</text>
    <text class="star" x="249" y="747" text-anchor="middle">★</text>
    <text class="star" x="273" y="747" text-anchor="middle">★</text>
    <text class="heading" x="421" y="748" text-anchor="middle">SECTION 6: CALL TO ACTION</text>
    <text class="star" x="564" y="747" text-anchor="middle">★</text>
    <text class="star" x="587" y="747" text-anchor="middle">★</text>
    <text class="star" x="609" y="747" text-anchor="middle">★</text>
    <line x1="47" y1="760" x2="799" y2="760" stroke="var(--red)"/>
  </g>

  <!-- Call to action panel -->
  <rect class="panel" x="47" y="767" width="752" height="223" fill="var(--navy)"/>
  <g class="call-to-action">
    <text class="cta-title" x="72" y="828">What Can</text>
    <text class="cta-title" x="72" y="860">You Do?</text>

    <text class="cta-head" x="224" y="866" fill="var(--gold)">Data</text>
    <line x1="224" y1="873" x2="368" y2="873" stroke="var(--gold)"/>
    <text class="cta-copy" x="223" y="896">Data points</text>
    <text class="cta-copy" x="223" y="915">Data points</text>
    <text class="cta-copy" x="223" y="934">Data points</text>
    <text class="cta-copy" x="223" y="953">Data points</text>

    <line x1="497" y1="807" x2="778" y2="807" stroke="var(--red)"/>
    <line x1="540" y1="907" x2="778" y2="907" stroke="var(--blue)"/>

    <circle cx="421" cy="903" r="61" fill="var(--gold)"/>
    <circle cx="487" cy="903" r="61" fill="var(--blue)"/>
    <circle cx="453" cy="846" r="61" fill="var(--red)"/>
    <circle cx="452" cy="900" r="29" fill="var(--navy)"/>

    <g class="icon-megaphone" fill="#fff">
      <polygon points="447,816 462,810 462,829 447,823"/>
      <rect x="450" y="823" width="4" height="7"/>
      <path d="M466,813 q4,6 0,12" fill="none" stroke="#fff" stroke-width="1.6"/>
    </g>
    <g class="icon-data">
      <circle cx="391" cy="896" r="9" fill="#fff"/>
      <line x1="397" y1="902" x2="408" y2="913" stroke="#fff" stroke-width="3.5" stroke-linecap="round"/>
      <g fill="var(--gold)"><rect x="386" y="896" width="2.4" height="5"/><rect x="390" y="893" width="2.4" height="8"/><rect x="394" y="890" width="2.4" height="11"/></g>
    </g>
    <g class="icon-gavel" fill="#fff">
      <rect x="496" y="908" width="18" height="8" rx="1.5" transform="rotate(30 505 912)"/>
      <line x1="506" y1="915" x2="520" y2="925" stroke="#fff" stroke-width="3" stroke-linecap="round"/>
      <rect x="485" y="927" width="18" height="5"/>
    </g>

    <text class="cta-head" x="589" y="803" fill="var(--red)">Awareness</text>
    <text class="cta-copy" x="589" y="826">Start the conversation.</text>
    <text class="cta-copy" x="589" y="844">Ask veterans how they're</text>
    <text class="cta-copy" x="589" y="861">REALLY doing.</text>

    <text class="cta-head" x="588" y="902" fill="var(--blue)">Legislation</text>
    <text class="cta-copy" x="588" y="928">Demand a bipartisan study</text>
    <text class="cta-copy" x="588" y="946">of veteran suicide</text>
  </g>

  <!-- Source -->
  <line x1="47" y1="996" x2="799" y2="996" stroke="var(--red)"/>
  <text x="53" y="1021" font-size="16.5" font-weight="700" fill="var(--ink)">SOURCE</text>
</svg>

<p class="source-copy">Lorem Ipsum is simply dummy text of the printing and typesetting industry. Lorem Ipsum has been the industry's standard dummy text ever since the 1500s, when an unknown printer took a galley of type and scrambled it to make a type specimen book. It has survived not only five centuries, but also the leap into electronic typesetting, remaining essentially unchanged.</p>
</div>
</body>
</html>
```